Therapy Games Business Needs a Flyer for Conference Bag

Kindle Path is an on-line business which provides resources and training for professionals who provide therapy to children and adolescents. I am putting a flyer into a conference bag and would like to let the conference attendees know about our resources which are all available online. The conference is called Bright Minds in Classrooms and attendees would by psychologists, school counsellors, and staff associated with student well-being.
The main products I would like promoted are games on social skills and anger management - including -Grumpy Gophers, Hint Tiles, Revved Out or Settling In, Feelings Lotto (all can be viewed at www.kindlepath.com.au).
The aim is to get them to the website to buy however signing up for the e-newsletter is very important.

Industry/Entity Type

Training

```html
<!DOCTYPE html>
<html lang="en">
<head>
<meta charset="utf-8">
<title>Kindle Path – Training Flyer</title>
<link href="https://fonts.googleapis.com/css2?family=Arimo:wght@400;700&display=swap" rel="stylesheet">
<style>
  :root {
    --green: #2a7b3f;
    --green-dark: #1f5e30;
    --brand-grey: #5d6063;
    --swoosh-teal: #2a9c8a;
    --swoosh-green: #6fb24a;
    --swoosh-rust: #c4522a;
    --paper: #ffffff;
    --photo-dark: #2b2b2b;
    --photo-light: #e6ece3;
  }
  * { box-sizing: border-box; margin: 0; padding: 0; }
  html, body { width: 927px; height: 1200px; overflow: hidden; background: var(--paper); }
  body { font-family: "Arimo", Arial, sans-serif; }
  .flyer { position: relative; width: 927px; height: 1200px; overflow: hidden; background: var(--paper); }

  .brand { position: absolute; top: 116px; left: 668px; display: flex; align-items: center; gap: 10px;
    color: var(--brand-grey); font-size: 30px; font-weight: 400; white-space: nowrap; }
  .brand-mark { width: 14px; height: 14px; background: var(--green); }

  .swoosh-field { position: absolute; left: 0; top: 520px; width: 927px; height: 680px; }

  .headline { position: absolute; left: 62px; top: 110px; font-size: 196px; font-weight: 700;
    color: var(--green); letter-spacing: -4px; line-height: 1; }
  .headline-tail { position: absolute; left: 377px; top: 240px; font-size: 29px; color: var(--green); }
  .topic { position: absolute; left: 85px; top: 306px; font-size: 29px; color: var(--green); }

  .game-list { position: absolute; left: 94px; top: 364px; list-style: none; }
  .game-list li { display: flex; align-items: center; height: 61.5px; font-size: 28px; color: var(--green); }
  .game-list svg { width: 30px; height: 30px; margin-right: 29px; flex: none; }

  .photo { position: absolute; }
  .photo-game { left: 335px; top: 700px; width: 210px; height: 185px; border-radius: 6px;
    background: linear-gradient(160deg, #3d5a3a, #d8b437 70%, #e9eee6); opacity: .85; }
  .photo-session { left: 545px; top: 528px; width: 345px; height: 385px; border-radius: 8px;
    background: radial-gradient(circle at 70% 30%, #d9d9d9 0 18%, transparent 40%),
                linear-gradient(180deg, var(--photo-light), var(--photo-dark) 55%); }

  .visit { position: absolute; top: 1024px; width: 100%; text-align: center; color: var(--paper); font-size: 24px; }
  .url-band { position: absolute; top: 1062px; left: 0; width: 100%; height: 66px; background: var(--paper);
    display: flex; align-items: center; justify-content: center; }
  .url { color: var(--green); font-size: 42px; font-weight: 700; letter-spacing: .5px; }
  .signup-band { position: absolute; top: 1130px; left: 0; width: 100%; height: 70px;
    background: linear-gradient(90deg, var(--green-dark), var(--swoosh-green) 50%, var(--green-dark));
    display: flex; align-items: center; justify-content: center; }
  .signup { color: var(--paper); font-size: 31px; }
</style>
</head>
<body>
<main class="flyer">
  <div class="swoosh-field" role="img" aria-label="Sweeping green, teal and rust ribbon curves across the lower page">
    <svg width="927" height="680" viewBox="0 0 927 680">
      <defs>
        <linearGradient id="field" x1="0" y1="0" x2="0" y2="1">
          <stop offset="0" stop-color="#ffffff"/>
          <stop offset=".45" stop-color="#e3efdc"/>
          <stop offset="1" stop-color="#7fb95c"/>
        </linearGradient>
        <linearGradient id="ribbon" x1="0" y1="0" x2="1" y2="1">
          <stop offset="0" stop-color="#2a9c8a"/>
          <stop offset=".5" stop-color="#c4522a" stop-opacity=".7"/>
          <stop offset="1" stop-color="#2a9c8a"/>
        </linearGradient>
      </defs>
      <path d="M0 0 Q120 260 927 300 L927 680 L0 680 Z" fill="url(#field)"/>
      <path d="M0 40 Q160 330 927 360 L927 420 Q150 400 0 160 Z" fill="url(#ribbon)" opacity=".55"/>
    </svg>
  </div>

  <div class="brand"><span class="brand-mark"></span>Kindle Path</div>

  <h1 class="headline">WE</h1>
  <p class="headline-tail">give training for games on</p>
  <h2 class="topic">Social skills &amp; Anger management</h2>

  <ul class="game-list">
    <li><svg viewBox="0 0 30 30"><circle cx="15" cy="15" r="13" fill="none" stroke="var(--green)" stroke-width="2"/><path d="M11 8 L20 15 L11 22 L13 15 Z" fill="var(--green)"/></svg>Grumpy Gophers,</li>
    <li><svg viewBox="0 0 30 30"><circle cx="15" cy="15" r="13" fill="none" stroke="var(--green)" stroke-width="2"/><path d="M11 8 L20 15 L11 22 L13 15 Z" fill="var(--green)"/></svg>Hint Tiles,</li>
    <li><svg viewBox="0 0 30 30"><circle cx="15" cy="15" r="13" fill="none" stroke="var(--green)" stroke-width="2"/><path d="M11 8 L20 15 L11 22 L13 15 Z" fill="var(--green)"/></svg>Revved Out or Settling In</li>
    <li><svg viewBox="0 0 30 30"><circle cx="15" cy="15" r="13" fill="none" stroke="var(--green)" stroke-width="2"/><path d="M11 8 L20 15 L11 22 L13 15 Z" fill="var(--green)"/></svg>Feelings Lotto</li>
  </ul>

  <div class="photo photo-game" role="img" aria-label="Boxed card game with loose playing cards and a card holder"></div>
  <div class="photo photo-session" role="img" aria-label="Silhouette of an adult and two children playing at a colourful board game easel"></div>

  <p class="visit">visit</p>
  <div class="url-band"><span class="url">www.kindlepath.com.au</span></div>
  <div class="signup-band"><span class="signup">Signup for e-newsletter</span></div>
</main>
</body>
</html>
```